Modern Venture Capital website

Design a modern website for a venture capital firm. This website should be modern and beautiful and be on par with other Venture Capital websites. I have a logo and a hero video I'd like to use. Link to hero video: https://filevault.example-share.net/file/d/9Q_7k2mzp4r8tn0W6XLfQkHa-BvvRNCT/view?usp=share_link

Preference will be given to the best design that combines design with the best images and digital content. That means no generic free stock videos 😅

I currently built a wix website to give you an idea of what content needs to be on the website. Depending on your design it can be 3 pages, or one long page. I will leave it up to you.

WEBSITE: https://marcel58274.sitebuilder-demo.net/my-site-4

Target Market(s)

Mid-career professionals, individuals interested in Venture Capital

Industry/Entity Type

Finance, venture capital, startups

Requirements
Must have
• must use the hero video I have and must use my logo. Must use high quality images that matches the website design - no generic stock images

```html
<!DOCTYPE html>
<html lang="en">
<head>
<meta charset="utf-8">
<title>Nightfall Capital — Venture Capital for the late night hustlers</title>
<link href="https://fonts.googleapis.com/css2?family=Poppins:wght@300;400;500;600;700;800&display=swap" rel="stylesheet">
<style>
:root{
  --orange:#ff6a3d;
  --orange-soft:#ff7c52;
  --ink:#111111;
  --black:#000000;
  --white:#ffffff;
  --muted:#444444;
  --card:#f4f4f4;
  --line:#dddddd;
}
*{box-sizing:border-box;margin:0;padding:0}
html,body{width:1200px;height:3567px;overflow:hidden}
body{font-family:"Poppins",sans-serif;color:var(--ink);background:var(--white);position:relative}
.abs{position:absolute}
.btn{position:absolute;display:flex;align-items:center;justify-content:center;background:var(--orange);color:var(--white);font-size:14px;font-weight:600;border-radius:4px;text-transform:uppercase;letter-spacing:.2px}
.brand{font-family:"Poppins",sans-serif;font-weight:700;color:var(--white);display:flex;align-items:center;gap:8px;line-height:1}
.brand-dot{width:10px;height:10px;border-radius:50%;background:var(--white)}

/* hero */
.hero{position:absolute;left:0;top:0;width:1200px;height:674px;overflow:hidden;
  background:radial-gradient(ellipse at 70% 75%,#4a3a22 0%,#1d1710 35%,#0a0908 70%),#000}
.nav a{position:absolute;top:48px;color:var(--white);font-size:15px;font-weight:500;text-decoration:none}
.hero-title{position:absolute;left:100px;top:172px;color:var(--white);line-height:1.05}
.hero-title .bold{font-size:62px;font-weight:800;display:block}
.hero-title .light{font-size:62px;font-weight:400;display:block;margin-top:8px}
.hero-title .accent{font-size:62px;font-weight:400;display:block;color:var(--orange);margin-top:4px}
.hero-sub{position:absolute;left:100px;top:478px;color:var(--white);font-size:20px}

/* become */
.become-title{position:absolute;left:97px;top:760px;font-size:58px;font-weight:400;line-height:1}
.become-title b{font-weight:800}
.become-copy{position:absolute;left:100px;top:850px;width:490px;font-size:16px;line-height:26px;color:var(--muted)}
.feature{position:absolute;left:100px;width:485px;display:flex;align-items:center;gap:22px}
.feature h3{font-size:20px;font-weight:500;line-height:29px;color:var(--ink)}
.feature-icon{width:58px;height:58px;flex:none;margin-left:32px}
.feature-card{position:absolute;left:100px;top:1050px;width:485px;height:276px;background:var(--card);border-radius:16px}
.feature-card h3{position:absolute;left:109px;top:36px;width:340px;font-size:20px;font-weight:500;line-height:29px}
.feature-card p{position:absolute;left:34px;top:140px;width:420px;font-size:15.5px;line-height:26px;color:var(--muted)}
.feature-card svg{position:absolute;left:34px;top:32px}
.divider{position:absolute;left:100px;top:1468px;width:440px;height:1px;background:var(--line)}

/* founders */
.founders{position:absolute;left:0;top:1708px;width:1200px;height:883px;
  background:linear-gradient(90deg,#0d0d0d 0%,#1a1a1a 30%,#121212 55%,#0b0b0b 100%)}
.founders-title{position:absolute;left:601px;top:1792px;color:var(--white);font-size:58px;font-weight:400;line-height:64px}
.founders-title b{font-weight:800}
.founders-copy{position:absolute;left:604px;top:2002px;width:500px;color:var(--white);font-size:16px;line-height:26.5px}
.founders-copy p+p{margin-top:12px}
.partners-line{position:absolute;left:100px;top:2383px;width:1004px;height:1px;background:#3a3a3a}
.partners-title{position:absolute;left:100px;top:2436px;color:var(--white);font-size:34px;line-height:40px;font-weight:400}
.partners-title b{font-weight:800}
.partner{position:absolute;top:2472px;color:var(--white);font-size:28px;font-weight:600;letter-spacing:1px}

/* economics */
.econ-title{position:absolute;left:0;width:1200px;top:2672px;text-align:center;font-size:58px;font-weight:400}
.econ-title b{font-weight:800}
.stat{position:absolute;top:2803px;width:201px;height:187px;background:var(--card);border-radius:12px;text-align:center}
.stat strong{display:block;margin-top:36px;font-size:54px;font-weight:800;color:var(--orange);line-height:1.1}
.stat span{display:block;margin-top:8px;font-size:17px;font-weight:500;color:var(--muted);line-height:23px}

/* footer */
.footer-left{position:absolute;left:0;top:3076px;width:600px;height:491px;background:var(--black)}
.footer-right{position:absolute;left:600px;top:3076px;width:600px;height:491px;
  background:linear-gradient(135deg,#ff7a4e 0%,#ff6234 50%,#f2582a 100%)}
.contact{position:absolute;left:100px;display:flex;gap:20px;color:var(--white);font-size:23px;line-height:31px}
.contact svg{flex:none;margin-top:4px}
.copyright{position:absolute;left:100px;top:3494px;color:var(--white);font-size:15px}
.cta-title{position:absolute;left:670px;top:3180px;color:var(--white);font-size:56px;line-height:58px;font-weight:400}
.cta-title b{font-weight:800}
.cta-sub{position:absolute;left:670px;top:3359px;color:var(--white);font-size:16px;font-weight:500}
</style>
</head>
<body>

<!-- Hero -->
<section class="hero" role="img" aria-label="Night city skyline with a full moon rising over the lights"></section>
<div class="brand abs" style="left:100px;top:36px;font-size:26px"><span>Nightfall Capital</span><span class="brand-dot"></span></div>
<nav class="nav">
  <a style="left:553px;font-weight:700">Home</a>
  <a style="left:634px">Join VC</a>
  <a style="left:727px">Startups</a>
  <a style="left:826px;color:#aaa">|</a>
  <a style="left:866px">Log in</a>
</nav>
<div class="btn" style="left:951px;top:33px;width:149px;height:49px">Get Started</div>
<h1 class="hero-title">
  <span class="bold">Venture</span>
  <span class="bold">Capital</span>
  <span class="light">for the late</span>
  <span class="accent">night hustlers</span>
</h1>
<p class="hero-sub">Become a Venture Capital Investor</p>
<div class="btn" style="left:100px;top:533px;width:148px;height:48px">Learn More</div>

<!-- Become a VC -->
<h2 class="become-title">Become <b>a VC</b></h2>
<p class="become-copy">At Nightfall Capital, we're opening the doors to a new kind of investor, mid-career professionals and aspiring VCs who want real skin in the game, not just exposure from the sidelines.</p>

<div class="feature" style="top:973px">
  <svg class="feature-icon" viewBox="0 0 58 58" fill="none" stroke="#222" stroke-width="1.6"><path d="M6 46c6-8 14-10 22-8h10c3 0 3 4 0 4H28"/><path d="M38 40l12-6c3-1 4 2 2 4L36 50H14"/><circle cx="30" cy="20" r="4"/><path d="M40 8l2 4 4 1-3 3 1 4-4-2-4 2 1-4-3-3 4-1z"/></svg>
  <h3>Hands on VC Work</h3>
</div>

<div class="feature-card">
  <svg width="56" height="56" viewBox="0 0 56 56" fill="none"><circle cx="30" cy="26" r="24" fill="#ffb59c"/><circle cx="28" cy="26" r="18" stroke="#222" stroke-width="1.6"/><path d="M28 15l3 7 7 1-5 5 1 7-6-3-6 3 1-7-5-5 7-1z" stroke="#222" stroke-width="1.6"/><path d="M14 40L4 50" stroke="#222" stroke-width="1.6"/></svg>
  <h3>Meaningful Opportunities to develop your career in Venture Capital</h3>
  <p>Nightfall Investors, depending on the level of commitment and involvement, can work at our fund as Partners, Principals, Senior Associates, Associates and Venture Partners.</p>
</div>

<div class="feature" style="top:1362px">
  <svg class="feature-icon" viewBox="0 0 58 58" fill="none" stroke="#222" stroke-width="1.6"><circle cx="30" cy="22" r="11"/><path d="M30 15v14M27 18h5a2 2 0 010 4h-4a2 2 0 000 4h5"/><path d="M6 44c6-6 12-7 20-5h8c3 0 3 4 0 4H26"/><path d="M34 43l12-5c3-1 4 2 2 4L34 52H12"/><path d="M30 4v5"/></svg>
  <h3>Earn Carry and Put Your Name on an Investment</h3>
</div>

<div class="divider"></div>

<div class="feature" style="top:1497px">
  <svg class="feature-icon" viewBox="0 0 58 58" fill="none" stroke="#222" stroke-width="1.6"><circle cx="29" cy="12" r="5"/><circle cx="20" cy="18" r="4"/><circle cx="38" cy="18" r="4"/><path d="M8 24c0 14 10 22 21 26 11-4 21-12 21-26"/><path d="M16 30c4 6 8 9 13 11 5-2 9-5 13-11"/></svg>
  <h3>Join a community of Hustlers</h3>
</div>

<svg class="abs" style="left:630px;top:800px" width="500" height="735" viewBox="0 0 500 735">
  <polygon points="18,5 495,225 470,715 35,735 42,450 6,455" fill="var(--orange-soft)"/>
</svg>
<div class="abs" role="img" aria-label="Weathered wooden signpost with arrows pointing in many directions" style="left:640px;top:895px;width:470px;height:600px;border-radius:8px;background:linear-gradient(160deg,#6e6e6e 0%,#3d3d3d 55%,#2a2a2a 100%);opacity:.92"></div>

<!-- Founders -->
<section class="founders"></section>
<div class="abs" role="img" aria-label="Dark office tower at night with a few orange lit windows" style="left:0;top:1708px;width:560px;height:675px;background:radial-gradient(ellipse at 38% 24%,#7a3516 0%,#2a1a12 22%,#151515 50%,#0e0e0e 100%)"></div>
<h2 class="founders-title">Simplifying<br>success <b>for</b><br><b>founders</b></h2>
<div class="founders-copy">
  <p>Our strength lies in our network. Our LPs and operating partners are all mid-to-senior level executives in their industries. They bring real-world corporate experience, offering strategic insights and operational support to help our portfolio companies scale efficiently.</p>
  <p>We cut through the noise and get to the core of your business fast. If we love what you're building, we'll move. If not, we'll tell you quickly and respectfully. That lets you make</p>
</div>
<div class="btn" style="left:605px;top:2253px;width:148px;height:49px">Learn More</div>
<div class="partners-line"></div>
<h3 class="partners-title">Our<br><b>Partners</b></h3>
<span class="partner" style="left:308px">KORVEX</span>
<span class="partner" style="left:560px">Quince</span>
<span class="partner" style="left:750px">Tallowby</span>
<span class="partner" style="left:980px;font-size:24px">ARBOR.LANE</span>

<!-- Fund Economics -->
<h2 class="econ-title">Fund <b>Economics</b></h2>
<div class="stat" style="left:62px"><strong>14</strong><span>Pre-Seed / Seed<br>Investments</span></div>
<div class="stat" style="left:278px"><strong>50K</strong><span>Check Size</span></div>
<div class="stat" style="left:494px"><strong>20%</strong><span>Carried Interest</span></div>
<div class="stat" style="left:709px"><strong>2.5%</strong><span>Management<br>Fee</span></div>
<div class="stat" style="left:924px"><strong>1M</strong><span>Fund Size</span></div>

<!-- Footer -->
<footer>
  <div class="footer-left"></div>
  <div class="footer-right" role="img" aria-label="Orange tinted facade of a high-rise building"></div>
  <div class="brand abs" style="left:102px;top:3160px;font-size:34px"><span>Nightfall Capital</span><span class="brand-dot"></span></div>
  <div class="contact" style="top:3267px">
    <svg width="24" height="24" viewBox="0 0 24 24"><path d="M5 2l4 1 2 5-3 2c1 3 4 6 7 7l2-3 5 2 1 4c-1 2-3 3-5 3C9 22 2 15 2 6c0-2 1-3 3-4z" fill="var(--orange)"/></svg>
    <span>+1-555-010-2040</span>
  </div>
  <div class="contact" style="top:3314px">
    <svg width="26" height="22" viewBox="0 0 26 22"><rect x="1" y="2" width="24" height="18" fill="var(--orange)"/><path d="M1 3l12 9 12-9" stroke="#000" stroke-width="2" fill="none"/></svg>
    <span>info@nightfallcapital.example</span>
  </div>
  <div class="contact" style="top:3361px">
    <svg width="24" height="28" viewBox="0 0 24 28"><path d="M12 1C6 1 2 5 2 11c0 7 10 16 10 16s10-9 10-16C22 5 18 1 12 1z" fill="var(--orange)"/><circle cx="12" cy="11" r="4" fill="#000"/></svg>
    <span>Nightfall Capital,<br>Address Comes Here</span>
  </div>
  <p class="copyright">2025 Nightfall Capital. All Rights Reserved.</p>

  <h2 class="cta-title">Ready to<br><b>start investing</b><br><b>as a VC?</b></h2>
  <p class="cta-sub">Book an interview to learn more and see if you qualify.</p>
  <div class="btn" style="left:670px;top:3424px;width:147px;height:47px;background:var(--black)">Learn More</div>
</footer>

</body>
</html>
```